Bright Pelvic Health Business Card

Need a business card for a surgical practice called Bright Pelvic Health. We have recently selected a logo (attached). The business card will need to have two formats:
1) One with the logo/physician name/ contact info on the front and location information on the back.
2) One in "appointment reminder card" style with the logo/ contact info/ date/ time on the front and the location information on the back.

The front side should include the following information:
- Logo
- Ravi K. Desai, MD FACOG
- phone: 469-555-0182
- fax: 1-469-555-0147
- email: admin@brightpelvic.example
- website: www.brightpelvichealth.example

The back side should have the office locations listed:
4812 Quarry Bend Dr, Plano, TX 75093
3650 Wrenfield Rd, Plano, TX 75025
2245 Brambleton Ln, Irving, TX 75038
915 S Garnet Ave B314, Dallas, TX 75201
1836 Tillman Pkwy, Grand Prairie, TX 75051
6417 Dorrance Way Dr, San Antonio, TX 78240
5920 Kessler Rd, Pasadena, TX 77504

Target Market(s)

1. Other physicians who might refer patients
2. Female patients

Industry/Entity Type

Business

Font styles to use
Other font styles liked:
• Tahoma for lettering

Requirements
Must have
• As per the instructions
Should not have
• No other images needed -- please try to keep font consistent with logo design. Can use Tahoma as the font for lettering.

```html
<!DOCTYPE html>
<html lang="en">
<head>
<meta charset="utf-8">
<title>Bright Pelvic Health – Business Card</title>
<link href="https://fonts.googleapis.com/css2?family=Roboto:wght@400;700&display=swap" rel="stylesheet">
<style>
  :root {
    --stage: #e4e2df;
    --blue-deep: #1f4fa6;
    --blue-mid: #1d6cc0;
    --blue-soft: #5a7fc6;
    --white: #ffffff;
    --brand-blue: #1d5fae;
    --accent-red: #e3242b;
  }
  * { margin: 0; padding: 0; box-sizing: border-box; }
  html, body { width: 1200px; height: 960px; overflow: hidden; }
  body {
    background: var(--stage);
    font-family: "Roboto", Tahoma, sans-serif;
    position: relative;
  }
  .card {
    position: absolute;
    left: 270px;
    width: 645px;
    height: 368px;
    overflow: hidden;
    box-shadow: 0 3px 8px rgba(0,0,0,.35);
  }

  /* Back side */
  .card--back {
    top: 84px;
    background: linear-gradient(100deg, var(--blue-deep) 0%, var(--blue-mid) 60%, #2a7ccc 100%);
    color: var(--white);
  }
  .back__brand {
    position: absolute;
    left: 32px; top: 178px;
    width: 230px;
    font-size: 22px;
    font-weight: 700;
    color: var(--white);
    line-height: 1.2;
    text-align: center;
  }
  .locations {
    position: absolute;
    left: 300px; top: 78px;
  }
  .locations__title {
    font-size: 20px;
    font-weight: 700;
    margin-bottom: 6px;
  }
  .locations__list {
    list-style: none;
    font-size: 15.5px;
    line-height: 25.7px;
  }
  .locations__list li::before {
    content: "•";
    display: inline-block;
    width: 16px;
  }
  .back__rule {
    position: absolute;
    left: 0; right: 0; top: 332px;
    height: 2px;
    background: var(--white);
  }
  .back__web {
    position: absolute;
    left: 58px; top: 323px;
    padding: 0 6px;
    font-size: 14px;
    background: #2356ae;
  }

  /* Front side */
  .card--front {
    top: 507px;
    background: var(--white);
  }
  .front__panel {
    position: absolute;
    inset: 0;
  }
  .front__brand {
    position: absolute;
    left: 330px; top: 98px;
    display: flex;
    align-items: center;
    gap: 10px;
    font-size: 25px;
    font-weight: 700;
    color: var(--brand-blue);
    white-space: nowrap;
  }
  .front__brand-dot {
    width: 14px; height: 14px;
    border-radius: 50%;
    background: var(--accent-red);
  }
  .physician {
    position: absolute;
    left: 32px; top: 192px;
    color: var(--white);
  }
  .physician__name { font-size: 19px; font-weight: 700; }
  .physician__title { font-size: 14px; margin-top: 4px; }
  .contact {
    position: absolute;
    left: 32px; top: 265px;
    list-style: none;
    color: var(--white);
    font-size: 14px;
    line-height: 18.7px;
  }
  .contact li { display: flex; align-items: center; gap: 13px; }
  .contact svg { width: 14px; height: 14px; flex: none; }
</style>
</head>
<body>

<section class="card card--back" aria-label="Card back: office locations">
  <div class="back__brand">Bright Pelvic Health</div>
  <div class="locations">
    <h2 class="locations__title">Office Locations :</h2>
    <ul class="locations__list">
      <li>4812 Quarry Bend Dr, Plano, TX 75093</li>
      <li>3650 Wrenfield Rd, Plano, TX 75025</li>
      <li>2245 Brambleton Ln, Irving, TX 75038</li>
      <li>915 S Garnet Ave B314, Dallas, TX 75201</li>
      <li>1836 Tillman Pkwy, Grand Prairie, TX 75051</li>
      <li>6417 Dorrance Way Dr, San Antonio, TX 78240</li>
      <li>5920 Kessler Rd, Pasadena, TX 77504</li>
    </ul>
  </div>
  <div class="back__rule"></div>
  <div class="back__web">www.brightpelvichealth.example</div>
</section>

<section class="card card--front" aria-label="Card front: physician and contact">
  <svg class="front__panel" width="645" height="368" viewBox="0 0 645 368" aria-hidden="true">
    <defs>
      <linearGradient id="frontBlue" x1="0" y1="0" x2="1" y2="0">
        <stop offset="0" stop-color="#1a5fb4"/>
        <stop offset="1" stop-color="#5a7fc6"/>
      </linearGradient>
    </defs>
    <path d="M0 0 H250 C300 120 330 240 300 368 H0 Z" fill="url(#frontBlue)"/>
  </svg>

  <div class="front__brand"><span class="front__brand-dot"></span>Bright Pelvic Health</div>

  <div class="physician">
    <h1 class="physician__name">Ravi K. Desai</h1>
    <p class="physician__title">MD FACOG</p>
  </div>

  <ul class="contact">
    <li>
      <svg viewBox="0 0 16 16" fill="#fff" aria-hidden="true"><path d="M1 5c0-2 2-3 7-3s7 1 7 3v1h-4V4.5H5V6H1z"/><rect x="3" y="7" width="10" height="7" rx="1"/></svg>
      469-555-0182
    </li>
    <li>
      <svg viewBox="0 0 16 16" fill="#fff" aria-hidden="true"><rect x="4" y="1" width="8" height="4"/><rect x="1" y="6" width="14" height="6" rx="1"/><rect x="4" y="10" width="8" height="5" fill="#4a74c2" stroke="#fff"/></svg>
      1-469-555-0147
    </li>
    <li>
      <svg viewBox="0 0 16 16" fill="none" stroke="#fff" stroke-width="1.5" aria-hidden="true"><rect x="1" y="3" width="14" height="10"/><path d="M1 3l7 6 7-6"/></svg>
      admin@brightpelvic.example
    </li>
    <li>
      <svg viewBox="0 0 16 16" fill="none" stroke="#fff" stroke-width="1.3" aria-hidden="true"><circle cx="8" cy="8" r="6.5"/><ellipse cx="8" cy="8" rx="3" ry="6.5"/><path d="M1.5 8h13M2.5 4.8h11M2.5 11.2h11"/></svg>
      www.brightpelvichealth.example
    </li>
  </ul>
</section>

</body>
</html>
```